Labels for fruit liqueur bottles

We are looking for a visual identity based on our logo, for fruit liqueur labels. To date, we have different liqueurs such as: lemon liqueur, orange liqueurs, mandarin liqueurs, grapefruit liqueurs. We will then create other liqueurs such as strawberry, apple or even apricot. Our goal is to have a single visual that we can adapt in different colors depending on the fruit used.

On the label there should be:
the logo
homemade
the name of the fruit (which can be changed depending on the product)
swiss-made
50cl
21°

Colors

Designer to choose colors to be used in the design.

Requirements
Must have
• a visual of liquor bottle labels, with the possibility of changing the background colors, depending on the fruit used
Nice to have
• something modern and nice to look at. We must be able to read the basic fruit in the blink of an eye. it is also possible to have a black or white or colored label background.

```html
<!DOCTYPE html>
<html lang="en">
<head>
<meta charset="utf-8">
<title>Don Vittorio – Orange Liqueur Label</title>
<link href="https://fonts.googleapis.com/css2?family=Bebas+Neue&family=Montserrat:wght@600;800&family=Teko:wght@400;500&display=swap" rel="stylesheet">
<style>
  :root {
    --fruit: #ff8300;
    --label-black: #000000;
    --frame-white: #ffffff;
    --band-red: #ff3d14;
    --band-text: #ffeccd;
    --text-white: #ffffff;
    --signature-grey: #4a4a4a;
  }
  * { margin: 0; padding: 0; box-sizing: border-box; }
  html, body { width: 1200px; height: 432px; overflow: hidden; }
  body { background: var(--fruit); font-family: "Teko", sans-serif; }

  .canvas { position: relative; width: 1200px; height: 432px; overflow: hidden; }

  .fruit-pattern {
    position: absolute; inset: 0;
    background: radial-gradient(ellipse at center, var(--fruit) 0%, var(--fruit) 60%, #ff8a10 100%);
  }

  .label-frame {
    position: absolute; left: 459px; top: 64px; width: 285px; height: 348px;
    border: 2.5px solid var(--frame-white);
  }
  .label {
    position: absolute; left: 469px; top: 73px; width: 264px; height: 330px;
    background: var(--label-black);
  }
  .brand-dot {
    position: absolute; left: 559px; top: 36px; width: 82px; height: 82px;
    border-radius: 50%; background: var(--band-red);
    border: 6px solid var(--frame-white);
  }

  .brand-name {
    position: absolute; left: 469px; top: 123px; width: 264px; text-align: center;
    font-family: "Montserrat", sans-serif; font-weight: 800; font-size: 26px;
    letter-spacing: -0.8px; color: var(--text-white); line-height: 1;
  }
  .brand-tagline {
    position: absolute; left: 469px; top: 151px; width: 264px; text-align: center;
    font-family: "Montserrat", sans-serif; font-weight: 600; font-size: 12.5px;
    letter-spacing: 0.6px; color: var(--text-white); line-height: 1;
  }

  .fruit-name {
    position: absolute; left: 469px; top: 198px; width: 264px; text-align: center;
    font-family: "Bebas Neue", sans-serif; font-weight: 400; font-size: 66px; line-height: 1;
    color: var(--fruit); letter-spacing: 0.5px;
  }
  .product-type {
    position: absolute; left: 469px; top: 255px; width: 264px; text-align: center;
    font-family: "Bebas Neue", sans-serif; font-weight: 400; font-size: 50px; line-height: 1;
    color: var(--text-white); transform: scaleX(0.88);
  }
  .product-rule { position: absolute; top: 276px; }
  .product-rule--left { left: 500px; }
  .product-rule--right { left: 665px; }

  .detail {
    position: absolute; font-size: 11.5px; line-height: 1; color: var(--text-white);
    text-transform: uppercase; white-space: nowrap; text-align: center;
  }
  .detail--batch { left: 491px; top: 331px; width: 57px; }
  .detail--crafter { left: 650px; top: 331px; width: 64px; }
  .detail-rule { position: absolute; height: 1px; background: var(--text-white); top: 343px; }
  .detail-rule--batch { left: 491px; width: 57px; }
  .detail-rule--crafter { left: 653px; width: 57px; }
  .bottle-number {
    position: absolute; left: 491px; top: 351px; font-size: 11px; color: var(--text-white);
    text-transform: uppercase; line-height: 1; white-space: nowrap;
  }
  .bottle-number em { font-style: italic; margin-left: 6px; }

  .swiss-flag { position: absolute; left: 590px; top: 316px; }
  .origin {
    position: absolute; left: 556px; top: 347px; width: 90px; text-align: center;
    font-size: 20px; line-height: 1; color: var(--text-white); white-space: nowrap;
  }

  .crafter-signature {
    position: absolute; left: 658px; top: 350px; width: 49px; height: 12px;
    background: var(--signature-grey); border-radius: 6px;
  }

  .spec-band {
    position: absolute; left: 469px; top: 370px; width: 264px; height: 33px;
    background: var(--band-red);
    display: flex; align-items: center; justify-content: center; gap: 14px;
    font-size: 18px; font-weight: 400; color: var(--band-text); padding-top: 3px;
    white-space: nowrap;
  }
  .spec-band .sep { width: 5px; height: 5px; background: var(--band-text); margin-top: -3px; }
</style>
</head>
<body>
<main class="canvas">
  <div class="fruit-pattern" role="img" aria-label="Line-drawn pattern of assorted fruits on orange"></div>

  <div class="label-frame"></div>
  <section class="label"></section>
  <div class="brand-dot"></div>

  <h1 class="brand-name">DON VITTORIO</h1>
  <p class="brand-tagline">liqueur de fruits</p>

  <h2 class="fruit-name">ORNAGE</h2>
  <svg class="product-rule product-rule--left" width="34" height="4" viewBox="0 0 34 4"><polygon points="0,2 34,0 34,4" fill="#fff"/></svg>
  <p class="product-type">LIQUEUR</p>
  <svg class="product-rule product-rule--right" width="34" height="4" viewBox="0 0 34 4"><polygon points="0,0 34,2 0,4" fill="#fff"/></svg>

  <p class="detail detail--batch">Small batch</p>
  <span class="detail-rule detail-rule--batch"></span>
  <p class="bottle-number">Bottle: <em>01/25</em></p>

  <svg class="swiss-flag" width="21" height="21" viewBox="0 0 20 20" aria-label="Swiss flag">
    <rect width="20" height="20" fill="#ff1a1a"/>
    <rect x="8" y="4" width="4" height="12" fill="#fff"/>
    <rect x="4" y="8" width="12" height="4" fill="#fff"/>
  </svg>
  <p class="origin">SWISS-MADE</p>

  <p class="detail detail--crafter">Master crafter:</p>
  <span class="detail-rule detail-rule--crafter"></span>
  <div class="crafter-signature" role="img" aria-label="Handwritten signature of the master crafter"></div>

  <div class="spec-band">
    <span>21% ABV</span><span class="sep"></span><span>HOMEMADE</span><span class="sep"></span><span>50CL</span>
  </div>
</main>
</body>
</html>
```